Rollers & Glides.com

Vertical Business Card with focus on branding with our icon. Information on card will be logo, persons name, position, phone number, email address and website. Use the the name Marcus Delby, position President, phone number 480.315.7792, email Marcus@rollersandglides-example.com, website www.rollersandglides-example.com.

```html
<!DOCTYPE html>
<html lang="en">
<head>
<meta charset="utf-8">
<title>Rollers &amp; Glides – Business Card</title>
<link href="https://fonts.googleapis.com/css2?family=Montserrat:wght@400;500;600&display=swap" rel="stylesheet">
<style>
  :root {
    --brand-blue: #2b67b1;
    --kraft: #c9ab82;
    --ink: #141414;
    --paper-white: #ffffff;
    --backdrop: #e6e8ec;
  }
  * { box-sizing: border-box; margin: 0; padding: 0; }
  html, body {
    width: 1200px;
    height: 960px;
    overflow: hidden;
    background: var(--backdrop);
    font-family: "Montserrat", sans-serif;
  }
  .stage {
    width: 1200px;
    height: 960px;
    display: flex;
    align-items: center;
    justify-content: center;
  }
  .business-card {
    width: 460px;
    height: 805px;
    display: flex;
    flex-direction: column;
    box-shadow: 0 6px 18px rgba(0,0,0,0.18);
  }
  .card-top {
    height: 208px;
    background: var(--brand-blue);
    display: flex;
    align-items: center;
    justify-content: center;
  }
  .brand-name--flipped {
    transform: rotate(180deg);
    color: var(--paper-white);
    font-weight: 600;
    font-size: 28px;
    letter-spacing: 0.5px;
    display: flex;
    align-items: center;
    gap: 12px;
  }
  .brand-dot {
    width: 22px;
    height: 22px;
    border-radius: 50%;
    background: var(--paper-white);
  }
  .card-middle {
    position: relative;
    height: 336px;
    background: var(--kraft);
    display: flex;
    align-items: flex-start;
    justify-content: center;
    gap: 18px;
    padding-top: 92px;
  }
  .fold-line {
    position: absolute;
    left: 0;
    right: 0;
    top: 193px;
    border-top: 2px dotted var(--ink);
  }
  .brand-ring {
    position: relative;
    width: 86px;
    height: 86px;
    margin-top: 58px;
    border-radius: 50%;
    border: 16px solid var(--ink);
    flex-shrink: 0;
  }
  .brand-name--feature {
    position: relative;
    color: var(--brand-blue);
    font-weight: 600;
    font-size: 38px;
    line-height: 1.1;
  }
  .card-bottom {
    flex: 1;
    background: var(--brand-blue);
    color: var(--paper-white);
    padding: 40px 40px 0 40px;
  }
  .person-name {
    text-align: right;
    font-weight: 500;
    font-size: 32px;
    letter-spacing: 0.3px;
  }
  .person-title {
    text-align: right;
    font-weight: 400;
    font-size: 24px;
    margin-top: 2px;
    letter-spacing: 0.4px;
  }
  .contact-list {
    list-style: none;
    margin-top: 30px;
    font-size: 17.5px;
    line-height: 26px;
    font-weight: 400;
    white-space: nowrap;
  }
</style>
</head>
<body>
  <main class="stage">
    <article class="business-card">
      <header class="card-top">
        <div class="brand-name--flipped">
          <span>Rollers &amp; Glides</span>
          <span class="brand-dot"></span>
        </div>
      </header>
      <section class="card-middle">
        <div class="fold-line"></div>
        <span class="brand-ring"></span>
        <span class="brand-name--feature">Rollers &amp;<br>Glides</span>
      </section>
      <section class="card-bottom">
        <h1 class="person-name">Marcus Delby</h1>
        <p class="person-title">President</p>
        <ul class="contact-list">
          <li>480.315.7792</li>
          <li>Marcus@rollersandglides-example.com</li>
          <li>www.rollersandglides-example.com</li>
        </ul>
      </section>
    </article>
  </main>
</body>
</html>
```